Used Car Dealer seeks an Amazing Business Card Design

We are looking for a business card design that incorporates our logo and grabs the attention of anyone we give the business card to.

Looking to use the same colors as the logo. Our Logo choice is the black background with Red and Silver/Grey Lettering.

We also would like to see some embossed designs.

Target Market(s)

Used Car Buyers, Automotive, Auto

Industry/Entity Type

Automotive

Contact Information for Business Card

BVEL7K
Gordon Whitlock
482 Tarrow Lane
Suite 207
Dunmore, GA 30419
Office (770) 555-0142
Cell (770) 555-0187
bvel7kga@quellmail.com
www.bvel7kga.com

Colors
ffffff
ee3036

Requirements
Must have
• Must include our logo (Black Background with Red and Silver/Grey Lettering)
Nice to have
• Embossed Design. Can be Single or Double Sided.

```html
<!DOCTYPE html>
<html lang="en">
<head>
<meta charset="utf-8">
<title>BVEL7K Business Card</title>
<link rel="stylesheet" href="https://fonts.googleapis.com/css2?family=Source+Sans+3:wght@400;600;700&display=swap">
<style>
  :root {
    --page: #e6e3df;
    --card: #000000;
    --red: #ee3036;
    --band-red: #ff0000;
    --white: #ffffff;
    --ink: #111111;
    --silver-light: #f2f2f2;
    --silver-mid: #c9c9c9;
    --silver-dark: #9a9a9a;
  }
  * { box-sizing: border-box; margin: 0; padding: 0; }
  html, body { width: 1200px; height: 987px; overflow: hidden; }
  body {
    background: var(--page);
    font-family: "Source Sans 3", "Myriad Pro", Arial, sans-serif;
    position: relative;
  }
  .card {
    position: absolute;
    left: 293px;
    width: 615px;
    height: 351px;
    background: var(--card);
    box-shadow: 0 3px 8px rgba(0,0,0,.35);
  }
  .card--front { top: 130px; }
  .card--back { top: 506px; }

  .brand-name {
    position: absolute;
    left: 0; right: 0;
    text-align: center;
    font-weight: 700;
    color: var(--red);
    letter-spacing: 1px;
  }
  .card--front .brand-name { top: 88px; font-size: 46px; line-height: 56px; }
  .card--back .brand-name { top: 132px; font-size: 40px; line-height: 50px; }

  .info-band {
    position: absolute;
    left: 0; right: 0;
    top: 202px;
    height: 128px;
    display: flex;
  }
  .info-band__person {
    width: 307px;
    background: var(--band-red);
    color: var(--ink);
    padding: 14px 0 0 35px;
  }
  .person-name {
    font-size: 22px;
    font-weight: 700;
    line-height: 26px;
    margin-bottom: 4px;
    color: #1a1a1a;
  }
  .address-line { font-size: 16.5px; line-height: 22.5px; color: #2a1a1a; }

  .info-band__contact {
    flex: 1;
    margin-left: 2px;
    background: radial-gradient(ellipse at 30% 30%, var(--silver-light) 0%, var(--silver-mid) 55%, var(--silver-dark) 100%);
    padding: 14px 28px 0 0;
  }
  .contact-line {
    display: flex;
    justify-content: flex-end;
    align-items: center;
    font-size: 16.5px;
    line-height: 23.5px;
    color: var(--ink);
  }
  .contact-line svg { width: 15px; height: 15px; margin-left: 13px; fill: var(--ink); }

  .back-url {
    position: absolute;
    left: 0; right: 0;
    top: 188px;
    text-align: center;
    color: var(--white);
    font-size: 15px;
    letter-spacing: 6.5px;
  }
</style>
</head>
<body>
  <section class="card card--front">
    <div class="brand-name">BVEL7K</div>
    <div class="info-band">
      <div class="info-band__person">
        <div class="person-name">GORDON WHITLOCK</div>
        <div class="address-line">482 Tarrow Lane</div>
        <div class="address-line">Suite 207</div>
        <div class="address-line">Dunmore, GA 30419</div>
      </div>
      <div class="info-band__contact">
        <div class="contact-line">(770) 555-0142
          <svg viewBox="0 0 24 24" aria-hidden="true"><path d="M6.6 10.8a15.1 15.1 0 0 0 6.6 6.6l2.2-2.2a1 1 0 0 1 1-.25 11.4 11.4 0 0 0 3.6.57 1 1 0 0 1 1 1V20a1 1 0 0 1-1 1A17 17 0 0 1 3 4a1 1 0 0 1 1-1h3.5a1 1 0 0 1 1 1c0 1.25.2 2.45.57 3.57a1 1 0 0 1-.25 1z"/></svg>
        </div>
        <div class="contact-line">(770) 555-0187
          <svg viewBox="0 0 24 24" aria-hidden="true"><path d="M7 1h10a2 2 0 0 1 2 2v18a2 2 0 0 1-2 2H7a2 2 0 0 1-2-2V3a2 2 0 0 1 2-2zm0 3v15h10V4zm5 16.2a1 1 0 1 0 0 .01z"/></svg>
        </div>
        <div class="contact-line">bvel7kga@quellmail.com
          <svg viewBox="0 0 24 24" aria-hidden="true"><path d="M2 5h20v14H2zm2 2v.5l8 5 8-5V7zm0 2.8V17h16V9.8l-8 5z"/></svg>
        </div>
        <div class="contact-line">www.bvel7kga.com
          <svg viewBox="0 0 24 24" aria-hidden="true"><path d="M12 2a10 10 0 1 0 0 20 10 10 0 0 0 0-20zm-1 17.9A8 8 0 0 1 4.1 10L9 15v1a2 2 0 0 0 2 2zm6.9-2.5A2 2 0 0 0 16 16h-1v-3a1 1 0 0 0-1-1H8v-2h2a1 1 0 0 0 1-1V7h2a2 2 0 0 0 2-2v-.4a8 8 0 0 1 2.9 12.8z"/></svg>
        </div>
      </div>
    </div>
  </section>

  <section class="card card--back">
    <div class="brand-name">BVEL7K</div>
    <div class="back-url">www.bvel7kga.com</div>
  </section>
</body>
</html>
```